Box insert for packaging of junior girls briefs

Need a insert to fit into our girls briefs packaging. Box is made of frosted plastic and measures 6 inches in width, 5 inches in height and 1.5 inches thick.

Box will have a open top flip as seen in photo of frosted envelope, same goes for closure.

Attached is a photo of a blank paper insert in a clear plastic box, that gives an idea as how I want it to look when inserted into the box. Note the small cutout of a brief to show what style this is. I would need to have same thing for hipster and bikini.
Design on packaging needs to be clean and sharp and appealing to junior girls and adults in their low 20's. Needs to be sophisticated but not provocative.
I'm uploading a EPS file of our logo. Basic logo layout should remain the same, however I'd like to see some creativity in making the logo more playful and young looking.
The front of the insert should have minimal information, maybe just size.
The back should contain information like website, contents, small size chart and country of origin (do in sample text).
Top of insert should have style number, size, logo and barcode. It can also have a picture (not cut out) of item style.

UPDATE: The front of the insert refers to the taller part and the back refers to the shorter part.

Plastic

• Must use our logo. It has been uploaded. Basic layout need to stay the same but you can change around the font and make it more playful. I might even consider a different color if it feels right.

```html
<!DOCTYPE html>
<html lang="en">
<head>
<meta charset="utf-8">
<title>Luvelle Girls Briefs – Box Insert</title>
<link rel="stylesheet" href="https://fonts.googleapis.com/css2?family=Questrial&family=Poiret+One&display=swap">
<style>
  :root {
    --pink-deep: #d9327e;
    --pink-hot: #e5107f;
    --pink-mid: #ee6fa8;
    --pink-soft: #f7b3cf;
    --pink-pale: #fbe0ea;
    --white: #ffffff;
    --ink: #111111;
    --grid: #9a9a9a;
    --cell: #e9e9e9;
    --peach: #f6c9b4;
    --grey: #a6a6a6;
  }
  * { box-sizing: border-box; margin: 0; padding: 0; }
  html, body { width: 1200px; height: 2200px; overflow: hidden; }
  body { font-family: "Questrial", sans-serif; background: var(--pink-mid); position: relative; }

  .panel { position: absolute; left: 0; width: 1200px; }
  .panel--back {
    top: 0; height: 800px;
    background: radial-gradient(ellipse at 15% 30%, var(--pink-pale) 0%, var(--pink-soft) 35%, var(--pink-mid) 75%, var(--pink-deep) 100%);
  }
  .panel--top {
    top: 800px; height: 400px;
    background: linear-gradient(90deg, var(--pink-pale) 0%, var(--pink-soft) 45%, var(--pink-mid) 100%);
  }
  .panel--front {
    top: 1200px; height: 868px;
    background: radial-gradient(ellipse at 20% 20%, var(--pink-pale) 0%, var(--pink-soft) 30%, var(--pink-mid) 65%, var(--pink-deep) 100%);
  }
  .panel--care {
    top: 2068px; height: 132px;
    background: var(--pink-deep);
    color: var(--white);
    font-size: 24px; line-height: 28px;
    text-align: center; padding: 12px 70px 0;
  }
  .panel--care strong { font-weight: 400; text-decoration: underline; }

  /* size chart, printed inverted for the back flap */
  .size-chart {
    position: absolute; left: 59px; top: 73px; width: 1097px; height: 525px;
    background: var(--white); padding: 26px 28px;
    transform: rotate(180deg);
  }
  .size-chart table { width: 100%; border-collapse: collapse; font-size: 15px; color: var(--ink); }
  .size-chart td, .size-chart th {
    border: 1.5px solid var(--grid); text-align: center; height: 54px; font-weight: 400;
  }
  .size-chart th { height: 30px; }
  .size-chart .unit td { height: 26px; background: var(--white); }
  .size-chart tbody.measure td:not(.label) { background: var(--cell); }
  .size-chart td.label { text-align: left; padding-left: 10px; width: 160px; }
  .size-chart td.num { width: 24px; border: none; font-size: 13px; }
  .size-chart .gap td { border: none; height: 18px; }
  .size-chart .note td { height: 28px; font-size: 13px; letter-spacing: .5px; }

  .size-title {
    position: absolute; left: 0; width: 1200px; top: 640px;
    text-align: center; font-family: "Poiret One", sans-serif;
    font-size: 92px; color: var(--white); letter-spacing: 6px;
    transform: rotate(180deg);
  }

  .brand { position: absolute; display: flex; align-items: center; justify-content: center;
    font-family: "Questrial", sans-serif; color: var(--ink); }
  .brand--top { left: 35px; top: 800px; width: 371px; height: 224px; font-size: 84px; }
  .brand--front { left: 340px; top: 1200px; width: 522px; height: 314px; font-size: 120px; }

  .product-label { position: absolute; background: var(--pink-hot); color: var(--white);
    font-family: "Questrial", sans-serif; text-align: center; }
  .product-label--top { left: 122px; top: 1024px; width: 193px; height: 161px; font-size: 54px; line-height: 64px; padding-top: 16px; }
  .product-label--front { left: 465px; top: 1514px; width: 271px; height: 227px; font-size: 78px; line-height: 92px; padding-top: 22px; }

  .art { position: absolute; border-radius: 40px; }
  .art--bikini { background: linear-gradient(180deg, var(--peach), #efb49b); opacity: .85; }
  .art--bandeau { background: linear-gradient(180deg, #d0d0d0, var(--grey)); opacity: .85; }
</style>
</head>
<body>

<section class="panel panel--back">
  <div class="size-chart">
    <table>
      <thead>
        <tr><th class="num"></th><th></th><th colspan="2">XS (5-6)</th><th colspan="2">S (7-8)</th><th colspan="2">M (10-12)</th><th colspan="2">L (14)</th><th colspan="2">XL (16)</th></tr>
      </thead>
      <tbody class="measure">
        <tr class="unit"><td class="num"></td><td class="label"></td><td>IN</td><td>CM</td><td>IN</td><td>CM</td><td>IN</td><td>CM</td><td>IN</td><td>CM</td><td>IN</td><td>CM</td></tr>
        <tr><td class="num">1.</td><td class="label">CHEST</td><td>25.5</td><td>65</td><td>27.5</td><td>70</td><td>29.5</td><td>75</td><td>32</td><td>81.5</td><td>34.5</td><td>88</td></tr>
        <tr><td class="num">2.</td><td class="label">SLEEVE LENGTH**</td><td>24.5</td><td>62.5</td><td>26.5</td><td>67.5</td><td>28.5</td><td>72.5</td><td>30.5</td><td>77.5</td><td>32.5</td><td>82.5</td></tr>
        <tr><td class="num">3.</td><td class="label">WAIST</td><td>22.5</td><td>57</td><td>24.5</td><td>62</td><td>26.5</td><td>67.5</td><td>28.5</td><td>72.5</td><td>31</td><td>79</td></tr>
        <tr><td class="num">4.</td><td class="label">HIP</td><td>25.5</td><td>65</td><td>27.5</td><td>70</td><td>29.5</td><td>75</td><td>32</td><td>81.5</td><td>34.5</td><td>88</td></tr>
        <tr><td class="num">5.</td><td class="label">INSEAM***</td><td>21</td><td>53.5</td><td>23</td><td>58.5</td><td>25.5</td><td>65</td><td>28.5</td><td>72</td><td>29.5</td><td>75</td></tr>
      </tbody>
      <tbody>
        <tr class="gap"><td colspan="12"></td></tr>
        <tr><td class="num">6.</td><td class="label">HEIGHT*</td><td>45</td><td>114</td><td>50</td><td>127</td><td>55</td><td>140</td><td>60</td><td>152.5</td><td>65</td><td>165</td></tr>
        <tr><td class="num"></td><td class="label">WEIGHT*</td><td>42-49 LBS</td><td>19-22 KG</td><td>52-68 LBS</td><td>23.5-31 KG</td><td>71-87 LBS</td><td>32-39.5 KG</td><td>87-100 LBS</td><td>39.5-45 KG</td><td>102-112 LBS</td><td>46-51 KG</td></tr>
        <tr class="note"><td colspan="12">*APPROXIMATE LENGTHS/WEIGHT &nbsp;**SLEEVE LENGTH FROM CENTER BACK NECK TO WRIST &nbsp;***INSEAM FROM ANKLE TO CROTCH</td></tr>
      </tbody>
    </table>
  </div>
  <div class="size-title">SIZE CHART</div>
</section>

<section class="panel panel--top"></section>
<div class="brand brand--top">LUVELLE</div>
<div class="product-label product-label--top">GIRLS<br>BRIEFS</div>
<div class="art art--bikini" role="img" aria-label="Illustration of a peach polka-dot bra and brief set" style="left:440px;top:873px;width:154px;height:257px;"></div>
<div class="art art--bandeau" role="img" aria-label="Illustration of a grey halter bandeau top and brief" style="left:631px;top:858px;width:183px;height:286px;"></div>

<section class="panel panel--front"></section>
<div class="brand brand--front">LUVELLE</div>
<div class="product-label product-label--front">GIRLS<br>BRIEFS</div>
<div class="art art--bikini" role="img" aria-label="Illustration of a peach polka-dot bra and brief set" style="left:139px;top:1672px;width:213px;height:382px;"></div>
<div class="art art--bandeau" role="img" aria-label="Illustration of a grey halter bandeau top and brief" style="left:792px;top:1592px;width:271px;height:418px;"></div>

<section class="panel panel--care">
  <strong>Washing Instructions</strong>: Rinse twice, minimize spinning to reduce creasing. Do not use powder detergents or any products that contain fabric softeners, conditioners, stain removers or bleach as they will affect garment performance. Do not wash with heavily soiled clothing. Line dry your garment, or tumble dry it on a warm, gentle cycle.
</section>

</body>
</html>
```